Business card design needed with logo

My business is called QVM Solutions & it is targeted towards mobile equipment maintenance in the Mining and civil industry. My work involves maintenance planning and maintenance management plus also supply tradespeople on a labour hire basis. We can provide from basic shut-down machine rebuild plans to complete rebuild services supply plans and labour to anywhere in Australia. I would like to use the colours Black, Red and Grey, I had done a desgin as attached but doesn't really explain what we do and gears don't embroider well onto shirts.
Updates

I also wanted to see the something replace the gears maybe just making the QVM lettering look a bit different or put together differently 

Hello I have extended the deadline by a few extra days as I would like to update details on the front of card, details below & can be put which ever way looks good;

Neil Patton
Director
0417562938
QVM@mailbrook.com.au
www.qvmsolutions-demo.com.au

On the back of the card I would like to have the below printed;

Capable of providing, but not limited to, across Australia:
- Contract Maintenance Planning.
- Skilled Mobile Maintenance labour hire.
- New machine build specifications. 
- Plant risk assessments and inspections.
- Shut down and rebuild program planning.
- Preventative maintenance tasks, including build of materials lists, creation and review.

Target Market(s)

Contractors and companies that use small and large earthmoving and mining machines

Industry/Entity Type

Business

Contact Information for Business Card

Trading name is QVM Solutions
My name and title is
Neil Patton Director
0417 562 938
QVM@mailbrook.com.au

Logo Text

QVM

```html
<!DOCTYPE html>
<html lang="en">
<head>
<meta charset="utf-8">
<title>QVM Solutions – Business Card</title>
<link rel="stylesheet" href="https://fonts.googleapis.com/css2?family=Open+Sans:wght@300;400&display=swap">
<style>
  :root {
    --page: #ffffff;
    --frame: #222222;
    --front-blue: #1784b5;
    --back-blue: #3a8cbd;
    --brand-blue: #1a86b7;
    --accent-red: #ed1c24;
    --ink: #111111;
    --white: #ffffff;
  }
  * { box-sizing: border-box; margin: 0; padding: 0; }
  html, body {
    width: 1016px; height: 1200px; overflow: hidden;
    background: var(--page);
    font-family: "Open Sans", "Segoe UI", sans-serif;
  }
  .sheet {
    position: relative; width: 1016px; height: 1200px;
    border: 1px solid var(--frame);
  }
  .card {
    position: absolute; left: 56px; width: 898px; height: 513px;
    border: 1px solid #444; overflow: hidden;
  }
  .card--front { top: 49px; background: var(--white); }
  .card--back { top: 636px; background: var(--back-blue); color: var(--white); }

  .front-panel { position: absolute; inset: 0; width: 100%; height: 100%; }
  .front-panel path { fill: var(--front-blue); }

  .brand-square { position: absolute; width: 100px; height: 100px; }
  .card--front .brand-square { left: 50px; top: 222px; background: var(--accent-red); }
  .card--back .brand-square { left: 500px; top: 50px; background: var(--white); }

  .wordmark { position: absolute; text-align: right; }
  .wordmark__name {
    display: block; font-weight: 300; font-size: 104px; line-height: 1;
    letter-spacing: 4px; margin-right: -4px;
  }
  .wordmark__tag { display: block; font-weight: 400; font-size: 36px; line-height: 1; margin-top: -3px; }

  .card--front .wordmark { right: 469px; top: 186px; }
  .card--front .wordmark__name { color: var(--brand-blue); }
  .card--front .wordmark__tag { color: var(--ink); }

  .contact-person {
    position: absolute; left: 688px; top: 25px;
    color: var(--white); font-size: 28px; line-height: 34.2px;
  }
  .contact-online {
    position: absolute; left: 440px; right: 0; top: 426px;
    text-align: center; color: var(--white); font-size: 28px; line-height: 34.2px;
  }

  .card--back .wordmark { right: 37px; top: 21px; color: var(--white); }
  .card--back .wordmark__tag { margin-top: -6px; }

  .service-list {
    position: absolute; left: 35px; top: 170px; list-style: none;
    font-size: 28px; line-height: 34.2px;
  }
  .service-list li { padding-left: 17px; text-indent: -17px; }
  .service-list li::before { content: "- "; }
  .back-web {
    position: absolute; right: 24px; top: 453px;
    font-size: 28px; line-height: 34.2px;
  }
</style>
</head>
<body>
<div class="sheet">
  <section class="card card--front">
    <svg class="front-panel" viewBox="0 0 898 513" preserveAspectRatio="none" aria-hidden="true">
      <path d="M410,0 Q554,258 406,513 L898,513 L898,0 Z"/>
    </svg>
    <span class="brand-square" aria-hidden="true"></span>
    <div class="wordmark">
      <span class="wordmark__name">QVM</span>
      <span class="wordmark__tag">Solutions</span>
    </div>
    <div class="contact-person">
      <p>Neil Patton</p>
      <p>Director</p>
      <p>0417562938</p>
    </div>
    <div class="contact-online">
      <p>QVM@mailbrook.com.au</p>
      <p>www.qvmsolutions-demo.com.au</p>
    </div>
  </section>

  <section class="card card--back">
    <span class="brand-square" aria-hidden="true"></span>
    <div class="wordmark">
      <span class="wordmark__name">QVM</span>
      <span class="wordmark__tag">Solutions</span>
    </div>
    <ul class="service-list">
      <li>Contract Maintenance Planning.</li>
      <li>Skilled Mobile Maintenance labour hire.</li>
      <li>New machine build specifications.</li>
      <li>Plant risk assessments and inspections.</li>
      <li>Shut down and rebuild program planning.</li>
      <li>Preventative maintenance tasks, including build<br>of materials lists, creation and review.</li>
    </ul>
    <p class="back-web">www.qvmsolutions-demo.com.au</p>
  </section>
</div>
</body>
</html>
```